Brightvolt Electrical Services Needs A Flyer Design

We need a flyer design for a new business based in Sydney, Australia called Brightvolt Electrical Services. We provide services for residential,commercial and industrial works. Services include Electrical Design, Installation, Repairs & Maintenance. Communications Installation, Cabling, Maintenance & Repairs. Over 25 years Industry Experience.Service Calls, Quick Response Time, Professional Service. We would like to see designs that use the colors red,white and blue similar to the logo. The final Design should be creative as the business logo suggests and should communicate the businesses services.

Target Market(s)

Residential

Industry/Entity Type

Industrial

Font styles to use
Sans Serif

Requirements
Must have
• My project must have the logo provided utilized in the flyer.It must list the following contact name and number Ray 0491 627 318 services as above in the project description. Flyer should be DL size (99mmx210mm).

```html
<!DOCTYPE html>
<html lang="en">
<head>
<meta charset="utf-8">
<title>Brightvolt Electrical Services – DL Flyer</title>
<link rel="stylesheet" href="https://fonts.googleapis.com/css2?family=Open+Sans:wght@600;700;800&family=Roboto+Condensed:wght@700&display=swap">
<style>
  :root {
    --backdrop: #ebebeb;
    --red: #cf2029;
    --blue: #233a80;
    --navy: #0e1a42;
    --white: #ffffff;
  }
  * { box-sizing: border-box; margin: 0; padding: 0; }
  html, body { width: 1200px; height: 1000px; overflow: hidden; }
  body { background: var(--backdrop); font-family: "Open Sans", Arial, sans-serif; position: relative; }

  .flyer { position: absolute; top: 88px; height: 800px; overflow: hidden; background: var(--white); }
  .flyer--front { left: 172px; width: 378px; }
  .flyer--services { left: 625px; width: 376px; }

  /* Front */
  .front-art { position: absolute; left: 0; top: 0; width: 378px; height: 680px; }
  .headline {
    position: absolute; left: 94px; width: 200px; top: 114px; text-align: center;
    font-family: "Roboto Condensed", Arial, sans-serif; font-weight: 700;
    color: var(--white); font-size: 32px; line-height: 34px;
  }
  .brand-footer {
    position: absolute; left: 0; bottom: 0; width: 100%; height: 120px;
    background: var(--white); display: flex; flex-direction: column;
    align-items: center; justify-content: center; color: var(--navy); font-weight: 800;
  }
  .brand-name { font-size: 34px; letter-spacing: 3px; line-height: 38px; }
  .brand-tag { font-size: 11px; letter-spacing: 2px; line-height: 16px; }

  /* Services */
  .services-title {
    height: 72px; background: var(--navy); color: var(--white);
    font-weight: 800; font-size: 35px; text-align: center; line-height: 72px;
  }
  .service-row { position: relative; height: 91.3px; display: flex; align-items: center; color: var(--white); font-weight: 700; font-size: 16px; line-height: 21px; }
  .service-row--blue { background: var(--blue); padding-left: 148px; }
  .service-row--red { background: var(--red); justify-content: flex-end; padding-right: 138px; text-align: right; }
  .service-photo {
    position: absolute; top: 0; height: 100%; width: 126px;
    background: linear-gradient(135deg, #c9ccd3, #6f7a8c);
  }
  .service-row--blue .service-photo { left: 0; clip-path: polygon(0 0, 82% 0, 100% 50%, 82% 100%, 0 100%); }
  .service-row--red .service-photo { right: 0; clip-path: polygon(12% 0, 100% 0, 100% 100%, 12% 100%, 0 50%); }

  .services-brand {
    height: 128px; background: var(--white); display: flex; flex-direction: column;
    align-items: center; padding-top: 30px; color: var(--navy); font-weight: 800;
  }
  .contact-band { position: absolute; left: 0; bottom: 0; width: 100%; height: 95px; }
  .contact-text {
    position: absolute; left: 0; bottom: 16px; width: 100%; text-align: center; color: var(--white); font-weight: 700;
  }
  .contact-label { font-size: 17px; line-height: 20px; }
  .contact-number { font-size: 27px; line-height: 34px; }
</style>
</head>
<body>

<section class="flyer flyer--front" aria-label="Flyer front">
  <svg class="front-art" viewBox="0 0 378 680" width="378" height="680">
    <polygon points="0,0 378,0 378,290 0,422" fill="var(--red)"/>
    <polygon points="0,422 378,290 378,680 0,680" fill="var(--blue)"/>
    <g class="illustration-area" role="img" aria-label="Light bulb outline with an electrician on a ladder fitting it">
      <circle cx="194" cy="167" r="100" fill="#ffffff" fill-opacity="0.10"/>
      <rect x="140" y="262" width="110" height="390" rx="10" fill="#ffffff" fill-opacity="0.08"/>
    </g>
    <defs>
      <path id="claim-arc" d="M 126,314 A 132 142 0 1 1 262,314"/>
    </defs>
    <text fill="#fff" font-family="Arial, sans-serif" font-weight="700" font-size="14.5">
      <textPath href="#claim-arc">Over 25 years Industry Experience.Service Calls, Quick Response Time, Professional Service</textPath>
    </text>
  </svg>
  <div class="headline">25 Years<br>Industry<br>Experience</div>
  <div class="brand-footer">
    <div class="brand-name">BRIGHTVOLT</div>
    <div class="brand-tag">ELECTRICAL SERVICES</div>
  </div>
</section>

<section class="flyer flyer--services" aria-label="Flyer services">
  <h1 class="services-title">OUR SERVICE</h1>
  <div class="service-row service-row--blue"><div class="service-photo" role="img" aria-label="Multimeter on electrical plans"></div>Electrical Design</div>
  <div class="service-row service-row--red"><div class="service-photo" role="img" aria-label="Hands installing a power outlet"></div>Electrical Instalation</div>
  <div class="service-row service-row--blue"><div class="service-photo" role="img" aria-label="Electrician testing a switchboard"></div>Electrical<br>Maintenance &amp; Repairs</div>
  <div class="service-row service-row--red"><div class="service-photo" role="img" aria-label="Technician working on a communications rack"></div>Communication Instalation</div>
  <div class="service-row service-row--blue"><div class="service-photo" role="img" aria-label="Rows of cable terminals"></div>Cabling Instalation</div>
  <div class="service-row service-row--red"><div class="service-photo" role="img" aria-label="Network patch panel with blue cables"></div>Communication &amp; Cabling<br>Maintenance &amp; Repairs</div>
  <div class="services-brand">
    <div class="brand-name">BRIGHTVOLT</div>
    <div class="brand-tag">ELECTRICAL SERVICES</div>
  </div>
  <svg class="contact-band" viewBox="0 0 376 95" width="376" height="95" preserveAspectRatio="none">
    <polygon points="0,0 188,0 376,28 376,95 0,95 0,28 188,0" fill="var(--navy)"/>
    <polygon points="0,0 376,0 376,28 188,0 0,28" fill="var(--white)"/>
  </svg>
  <div class="contact-text">
    <div class="contact-label">Contact:</div>
    <div class="contact-number">(Ray) 0491 627 318</div>
  </div>
</section>

</body>
</html>
```